Business Card Design

Buy and sell properties
Buy and rehab properties
Buy properties for cash
That is what I do but do need a logo
looking for some type of logo or design on it
Just started business
Back of card should say something like BUY HOUSES CASH
Overview: it is a new company. Basically I buy properties wholesale and fix them up and sell them or sell them to other fix and flippers
Background: company is new so not any background
Market: is basically anyone selling a house or buying a house. Someone that needs to sell house fast. Basically I am a cash home buyer!!!

Updates
Email on card should be:   harborlanerealtyinc@mailbox.test

Industry/Entity Type
House
Contact Information for Business Card
Harbor Lane Realty Inc
PO Box 718269
Cedar Marsh FL 32987

Dale Morrick
harborlanerealtyinc@mailbox.test
555-271-6094

```html
<!DOCTYPE html>
<html lang="en">
<head>
<meta charset="utf-8">
<title>Harbor Lane Realty Inc — Business Card</title>
<link href="https://fonts.googleapis.com/css2?family=Open+Sans:wght@400;600;700&display=swap" rel="stylesheet">
<style>
  :root {
    --backdrop: #d9d9d9;
    --card: #4f4f50;
    --band: #eeeeec;
    --brand-red: #d3102c;
    --contact-green: #1f9a3c;
    --tagline: #f2f2f2;
  }
  * { box-sizing: border-box; margin: 0; padding: 0; }
  html, body {
    width: 1200px;
    height: 1000px;
    overflow: hidden;
    background: var(--backdrop);
    font-family: "Open Sans", sans-serif;
  }
  .canvas {
    position: relative;
    width: 1200px;
    height: 1000px;
  }
  .card {
    position: absolute;
    left: 220px;
    width: 760px;
    height: 434px;
    background: var(--card);
    overflow: hidden;
    box-shadow: 0 6px 18px rgba(0,0,0,0.18);
  }
  .card--back { top: 36px; }
  .card--front { top: 526px; }

  .brand {
    position: absolute;
    display: flex;
    align-items: center;
  }
  .brand-mark {
    flex: none;
    background: var(--brand-red);
  }
  .brand-name {
    color: var(--brand-red);
    font-weight: 600;
    text-transform: uppercase;
    line-height: 1.05;
  }

  /* Back side */
  .back-block {
    position: absolute;
    left: 190px;
    top: 120px;
    width: 520px;
  }
  .back-block .brand { position: static; gap: 22px; }
  .back-block .brand-mark { width: 86px; height: 86px; }
  .back-block .brand-name { font-size: 46px; }
  .tagline {
    margin-top: 18px;
    margin-left: 108px;
    color: var(--tagline);
    font-size: 22px;
    font-weight: 600;
    letter-spacing: 0.28em;
  }

  /* Front side */
  .band {
    position: absolute;
    left: 0;
    background: var(--band);
    color: var(--contact-green);
    display: flex;
    align-items: center;
    white-space: nowrap;
  }
  .band--name {
    top: 62px; height: 50px; width: 440px;
    justify-content: center;
    font-size: 24px; font-weight: 700;
  }
  .band--phone {
    top: 134px; height: 40px; width: 430px;
    justify-content: center;
    font-size: 19px;
  }
  .band--email {
    top: 196px; height: 40px; width: 460px;
    justify-content: center;
    font-size: 18px;
  }
  .band--address {
    top: 316px; height: 48px; width: 100%;
    padding-left: 28px;
    font-size: 21px;
  }
  .card--front .brand {
    left: 490px;
    top: 150px;
    width: 250px;
    gap: 12px;
  }
  .card--front .brand-mark { width: 46px; height: 46px; }
  .card--front .brand-name { font-size: 27px; }
</style>
</head>
<body>
  <main class="canvas">
    <section class="card card--back" aria-label="Card back">
      <div class="back-block">
        <div class="brand">
          <span class="brand-mark" aria-hidden="true"></span>
          <p class="brand-name">Harbor Lane<br>Realty Inc</p>
        </div>
        <p class="tagline">BUY HOUSES CASH</p>
      </div>
    </section>

    <section class="card card--front" aria-label="Card front">
      <p class="band band--name">Dale Morrick</p>
      <p class="band band--phone">Phone : 555-271-6094</p>
      <p class="band band--email">Email : harborlanerealtyinc@mailbox.test</p>
      <div class="brand">
        <span class="brand-mark" aria-hidden="true"></span>
        <p class="brand-name">Harbor Lane<br>Realty Inc</p>
      </div>
      <p class="band band--address">Harbor Lane Realty Inc, PO Box : 718269, Cedar Marsh, FL 32987</p>
    </section>
  </main>
</body>
</html>
```